The Juniper Coach

I am a life coach specializing in helping people with depression and bipolar disorder. I would like a nice, fun design for a business card.

```html
<!DOCTYPE html>
<html lang="en">
<head>
<meta charset="utf-8">
<title>The Juniper Coach – Business Card</title>
<link href="https://fonts.googleapis.com/css2?family=Gelasio:wght@400;700&display=swap" rel="stylesheet">
<style>
  :root {
    --page-bg: #e9e6e2;
    --card-top: #f4f3f5;
    --card-mid: #dcdae0;
    --navy: #1f1d45;
    --navy-deep: #15133a;
    --ink: #1d1b40;
    --muted: #6b6870;
    --contact: #cfc9d3;
  }
  * { margin: 0; padding: 0; box-sizing: border-box; }
  html, body { width: 1200px; height: 970px; overflow: hidden; }
  body {
    background: var(--page-bg);
    font-family: "Gelasio", Georgia, serif;
    position: relative;
  }
  .business-card {
    position: absolute;
    left: 100px; top: 200px;
    width: 1000px; height: 571px;
    border-radius: 30px;
    overflow: hidden;
    background: linear-gradient(160deg, var(--card-top) 0%, #ebeaee 45%, var(--card-mid) 100%);
    box-shadow: 0 18px 40px rgba(40, 30, 30, 0.22);
  }
  .card-band { position: absolute; inset: 0; width: 100%; height: 100%; }
  .brand {
    position: absolute; left: 64px; top: 128px;
    display: flex; align-items: center; gap: 22px;
  }
  .brand-dot {
    width: 62px; height: 62px; border-radius: 50%;
    background: var(--navy);
  }
  .brand-name {
    font-size: 50px; font-weight: 400; color: var(--ink);
    letter-spacing: 0.2px;
  }
  .person {
    position: absolute; right: 46px; top: 72px; text-align: right;
  }
  .person-name { font-size: 31px; font-weight: 700; color: var(--ink); line-height: 1.1; }
  .person-title { font-size: 21px; color: var(--muted); line-height: 1.2; }
  .contact {
    position: absolute; right: 46px; top: 352px; text-align: right;
    color: var(--contact); font-size: 22px;
  }
  .address { line-height: 31px; margin-bottom: 12px; }
  .contact-row {
    display: flex; justify-content: flex-end; align-items: center;
    gap: 10px; height: 35px;
  }
  .contact-icon { width: 28px; height: 28px; flex: none; }
</style>
</head>
<body>
  <div class="business-card">
    <svg class="card-band" viewBox="0 0 1000 571" preserveAspectRatio="none" role="img" aria-label="Navy wave band across the lower card">
      <defs>
        <linearGradient id="bandFill" x1="0" y1="0" x2="1" y2="1">
          <stop offset="0" stop-color="#2a2856"/>
          <stop offset="1" stop-color="#15133a"/>
        </linearGradient>
      </defs>
      <path d="M0 470 C 300 500, 600 280, 1000 268 L1000 571 L0 571 Z" fill="url(#bandFill)"/>
    </svg>

    <div class="brand">
      <span class="brand-dot"></span>
      <span class="brand-name">The Juniper Coach</span>
    </div>

    <div class="person">
      <div class="person-name">Elena Marsh</div>
      <div class="person-title">President &amp; CEO</div>
    </div>

    <div class="contact">
      <div class="address">PO BOX 48, Willow Road<br>3rd Lane, Bristol</div>
      <div class="contact-row">
        <span>(204) 555 0187</span>
        <svg class="contact-icon" viewBox="0 0 28 28" aria-label="Phone" role="img">
          <circle cx="14" cy="14" r="12.5" fill="none" stroke="var(--contact)" stroke-width="1.5"/>
          <path d="M8 11 Q14 7 20 11 L18.5 13 L16.5 12 L16 10.5 Q14 10 12 10.5 L11.5 12 L9.5 13 Z M10 14 H18 L19 19 H9 Z" fill="var(--contact)"/>
        </svg>
      </div>
      <div class="contact-row">
        <span>hello@junipercoach.com</span>
        <svg class="contact-icon" viewBox="0 0 28 28" aria-label="Email" role="img">
          <circle cx="14" cy="14" r="12.5" fill="none" stroke="var(--contact)" stroke-width="1.5"/>
          <rect x="8" y="10" width="12" height="8.5" fill="var(--contact)"/>
          <path d="M8 10 L14 15 L20 10" fill="none" stroke="var(--navy)" stroke-width="1.2"/>
        </svg>
      </div>
      <div class="contact-row">
        <span>www.junipercoach.com</span>
        <svg class="contact-icon" viewBox="0 0 28 28" aria-label="Website" role="img">
          <circle cx="14" cy="14" r="12.5" fill="none" stroke="var(--contact)" stroke-width="1.5"/>
          <circle cx="14" cy="14" r="6.5" fill="none" stroke="var(--contact)" stroke-width="1.2"/>
          <ellipse cx="14" cy="14" rx="3" ry="6.5" fill="none" stroke="var(--contact)" stroke-width="1"/>
          <path d="M7.5 14 H20.5" stroke="var(--contact)" stroke-width="1"/>
        </svg>
      </div>
    </div>
  </div>
</body>
</html>
```